Talvero Networks LLC
Consultant, Health Care Operations
Talvero Networks LLC -
Creative Brief
Use specific fonts
I like Calibri, Tahoma, Lucida (rounded but professional) but am open to other similar fonts
Simple
Dwight Pennock
President, CEO
PO BOX 418263 Marlowe Bay, FL 32904
dwight@talverohub.com
talverohub.com

```html
<!DOCTYPE html>
<html lang="en">
<head>
<meta charset="utf-8">
<title>Talvero Networks LLC – Business Card</title>
<link rel="stylesheet" href="https://fonts.googleapis.com/css2?family=Open+Sans:wght@400;600;700&display=swap">
<style>
  :root {
    --page-bg: #ece9e4;
    --card-bg: #ffffff;
    --brand-blue: #1aa3e0;
    --brand-blue-deep: #0d7fc2;
    --ink: #1c1c1c;
    --ink-soft: #2f2f2f;
    --band-dark: #111111;
  }
  * { box-sizing: border-box; margin: 0; padding: 0; }
  html, body {
    width: 1200px;
    height: 935px;
    overflow: hidden;
    background: var(--page-bg);
    font-family: "Open Sans", Tahoma, sans-serif;
  }
  .canvas {
    position: relative;
    width: 1200px;
    height: 935px;
  }
  .business-card {
    position: absolute;
    left: 80px;
    top: 190px;
    width: 1040px;
    height: 556px;
    background: var(--card-bg);
    border-radius: 44px;
    overflow: hidden;
    box-shadow: 0 10px 28px rgba(0,0,0,0.18);
  }
  .brand-block {
    position: absolute;
    left: 40px;
    top: 60px;
    width: 460px;
    text-align: center;
  }
  .brand-dot {
    display: block;
    width: 200px;
    height: 200px;
    margin: 0 auto 40px;
    border-radius: 50%;
    background: var(--brand-blue);
  }
  .brand-name {
    font-size: 38px;
    font-weight: 700;
    line-height: 1.15;
    white-space: nowrap;
    color: var(--ink-soft);
  }
  .holder {
    position: absolute;
    left: 584px;
    top: 110px;
  }
  .holder-name {
    font-size: 36px;
    font-weight: 700;
    color: var(--brand-blue-deep);
    line-height: 1.1;
  }
  .holder-title {
    margin-top: 10px;
    font-size: 21px;
    color: var(--ink-soft);
  }
  .contact-list {
    position: absolute;
    left: 584px;
    top: 272px;
    list-style: none;
    font-size: 28px;
    line-height: 35px;
    color: var(--ink);
  }
  .card-band {
    position: absolute;
    left: 0;
    bottom: 0;
    width: 1040px;
    height: 60px;
  }
</style>
</head>
<body>
  <main class="canvas">
    <article class="business-card">
      <div class="brand-block">
        <span class="brand-dot"></span>
        <p class="brand-name">Talvero Networks LLC</p>
      </div>

      <header class="holder">
        <h1 class="holder-name">Dwight Pennock</h1>
        <p class="holder-title">President, CEO</p>
      </header>

      <ul class="contact-list">
        <li>PO BOX 418263</li>
        <li>Marlowe Bay, FL 32904</li>
        <li>Phone : 555.014.2290</li>
        <li>Email : dwight@talverohub.com</li>
        <li>Web : talverohub.com</li>
      </ul>

      <svg class="card-band" viewBox="0 0 1040 60" preserveAspectRatio="none" aria-hidden="true">
        <defs>
          <linearGradient id="band-blue" x1="0" y1="0" x2="1" y2="0">
            <stop offset="0" stop-color="#0d7fc2"/>
            <stop offset="0.6" stop-color="#27b2ec"/>
            <stop offset="1" stop-color="#0d7fc2"/>
          </linearGradient>
        </defs>
        <path d="M0 8 Q420 -4 720 6 L690 60 L0 60 Z" fill="url(#band-blue)"/>
        <path d="M720 6 Q900 0 1040 2 L1040 60 L690 60 Z" fill="var(--band-dark)"/>
      </svg>
    </article>
  </main>
</body>
</html>
```